New Stationery New Logo for KT Mouldings Limited

We have a new logo and now want new stationary to go with it

This will be

Letterhead
Compliments Slip
Business Cards

Company details are
KT Mouldings Limited
Brindle Row, Rugby, Warwickshire, CV34 7HX, UK
Telephone : +44(0)1788 930467
Fax: +44(0)1788 918723
Email: sales@ktmouldings.example
Web: www.ktmouldings.example

Target Market(s)

Engineering / Metal Stamping

Industry/Entity Type

Manufacture

Contact Information for Business Card

Neil Garbutt
Business Development Manager
KT Mouldings Limited
Brindle Row
Rugby
Warwickshire
CV34 7HX, UK

T: +44(0)1788 930467
F: +44(0)1788 918723
E: sales@ktmouldings.example
W: www.ktmouldings.example

Font styles to use
Sans Serif

Colors
33a6d7
0555a3
3176b5
85cae6
85acd3

Requirements
Must have
• Logo

```html
<!DOCTYPE html>
<html lang="en">
<head>
<meta charset="utf-8">
<title>KT Mouldings Limited – Business Card</title>
<link href="https://fonts.googleapis.com/css2?family=Arimo:wght@400;500&display=swap" rel="stylesheet">
<style>
  :root {
    --backdrop: #e6e6e4;
    --card-dark: #1c1c1e;
    --card-light: #ffffff;
    --brand-blue: #0555a3;
    --mid-blue: #3176b5;
    --text-grey: #55585c;
  }
  * { box-sizing: border-box; margin: 0; padding: 0; }
  html, body {
    width: 1200px; height: 716px; overflow: hidden;
    background: var(--backdrop);
    font-family: "Arimo", Arial, sans-serif;
  }
  .stage {
    position: relative; width: 1200px; height: 716px;
    display: flex; align-items: center; justify-content: center; gap: 48px;
  }
  .card {
    position: relative; width: 525px; height: 300px; overflow: hidden;
    box-shadow: 0 10px 28px rgba(0,0,0,.18);
  }
  /* back of card */
  .card-back {
    background: var(--card-dark);
    display: flex; flex-direction: column; align-items: center; justify-content: center;
  }
  .back-wordmark {
    display: flex; align-items: center; gap: 14px;
    color: var(--mid-blue); font-size: 30px; font-weight: 500;
    letter-spacing: 8px;
  }
  .back-wordmark .dot {
    width: 14px; height: 14px; border-radius: 50%; background: var(--mid-blue);
  }
  .back-web {
    margin-top: 34px; color: var(--brand-blue); font-size: 16px;
  }
  /* front of card */
  .card-front { background: var(--card-light); }
  .top-band {
    position: absolute; top: 0; left: 0; right: 0; height: 10px;
    background: var(--brand-blue);
  }
  .front-wordmark {
    position: absolute; left: 150px; top: 58px;
    display: flex; align-items: center; gap: 10px;
    color: var(--mid-blue); font-size: 24px; font-weight: 500;
  }
  .front-wordmark .dot {
    width: 12px; height: 12px; background: var(--mid-blue);
  }
  .person {
    position: absolute; left: 250px; top: 150px;
  }
  .person-name {
    color: var(--brand-blue); font-size: 21px; letter-spacing: .5px;
  }
  .person-role {
    color: var(--text-grey); font-size: 15px; margin-top: 2px;
  }
  .address {
    position: absolute; left: 28px; top: 192px;
    font-style: normal; font-size: 14px; line-height: 1.35; color: var(--text-grey);
  }
  .address .company { color: var(--brand-blue); }
  .divider {
    position: absolute; left: 238px; top: 218px; width: 2px; height: 56px;
    background: var(--brand-blue);
  }
  .contact {
    position: absolute; left: 254px; top: 216px;
    display: grid; grid-template-columns: auto auto; column-gap: 12px;
    font-size: 14px; line-height: 1.35;
  }
  .contact dt { color: var(--brand-blue); }
  .contact dd { color: var(--text-grey); }
</style>
</head>
<body>
<main class="stage">
  <section class="card card-back" aria-label="Business card back">
    <div class="back-wordmark"><span class="dot"></span>KT MOULDINGS</div>
    <p class="back-web">www.ktmouldings.example</p>
  </section>

  <section class="card card-front" aria-label="Business card front">
    <div class="top-band"></div>
    <div class="front-wordmark"><span class="dot"></span>KT Mouldings</div>
    <div class="person">
      <p class="person-name">PIETER VANDERMEER</p>
      <p class="person-role">Creative Director</p>
    </div>
    <address class="address">
      <span class="company">KT Mouldings Limited</span><br>
      Brindle Row, Rugby,<br>
      Warwickshire, CV34 7HX, UK
    </address>
    <div class="divider"></div>
    <dl class="contact">
      <dt>PHONE</dt><dd>+44(0)1788 930467</dd>
      <dt>FAX</dt><dd>+44(0)1788 918723</dd>
      <dt>EMAIL</dt><dd>sales@ktmouldings.example</dd>
    </dl>
  </section>
</main>
</body>
</html>
```